Mental Health Awareness License Plates

Below is the sample format I will need. That of a plain license plate w/o frame
*refer to image with name Licence wo Frame*
Delete Frame
Replace QR Code with “MO”
Replace 2025 sticker with “ YR
Use License Plate font (attached)
On Ribbon, keep the green background
The California front leg, needs to be gradated like a sunset and retain shape of CA
Palm trees sharpened
I need the files in a format that can be used on a website, printed or made into a poster.
One file that reads SAMPLE, one version that reads “NEWPLA8”d
The finished product should look like a license plate as shown in the example
*refer to image name finished product*
I want to clarify what we are looking for. The license plate design has been approved by the state, but we need a high res version of it in multiple file formats. The most important change we are looking for is to the ribbon. The palm trees against the sunset are fuzzy, we need those placed in front of an sunset on the front leg of the ribbon. The rear leg needs to remain green (mental health color). I hope this help clarify our design need.

```html
<!DOCTYPE html>
<html lang="en">
<head>
<meta charset="utf-8">
<title>Mental Health Awareness License Plate</title>
<link rel="stylesheet" href="https://fonts.googleapis.com/css2?family=Montserrat:wght@700&family=Oswald:wght@500&display=swap">
<style>
  :root {
    --backdrop: #24496a;
    --plate: #b0f7e8;
    --ink: #24496a;
    --state-orange: #f7941d;
    --ribbon-green: #1fa31a;
    --ribbon-sun: #f9a800;
    --ribbon-sand: #f6d58a;
  }
  html, body {
    margin: 0;
    padding: 0;
    width: 1200px;
    height: 853px;
    overflow: hidden;
    background: var(--backdrop);
  }
  .plate-canvas {
    display: block;
    width: 1200px;
    height: 853px;
  }
  .plate-body { fill: var(--plate); }
  .mount-hole { fill: var(--ink); }
  .state-name {
    font-family: "Montserrat", sans-serif;
    font-weight: 700;
    font-size: 104px;
    fill: var(--state-orange);
  }
  .plate-number {
    font-family: "Oswald", sans-serif;
    font-weight: 500;
    font-size: 284px;
    fill: var(--ink);
  }
  .plate-slogan {
    font-family: "Montserrat", sans-serif;
    font-weight: 700;
    font-size: 33px;
    fill: var(--ink);
  }
</style>
</head>
<body>
<svg class="plate-canvas" viewBox="0 0 1200 853" xmlns="http://www.w3.org/2000/svg">
  <defs>
    <linearGradient id="ribbon-tones" x1="0" y1="0" x2="1" y2="1">
      <stop offset="0" stop-color="var(--ribbon-sun)"/>
      <stop offset="0.55" stop-color="var(--ribbon-sun)"/>
      <stop offset="0.8" stop-color="var(--ribbon-sand)"/>
      <stop offset="1" stop-color="var(--ribbon-green)"/>
    </linearGradient>
  </defs>

  <rect class="plate-body" x="50" y="155" width="1090" height="543" rx="46"/>

  <circle class="mount-hole" cx="228" cy="215" r="22"/>
  <circle class="mount-hole" cx="964" cy="215" r="22"/>
  <circle class="mount-hole" cx="228" cy="632" r="22"/>
  <circle class="mount-hole" cx="964" cy="632" r="22"/>

  <text class="state-name" x="345" y="294" textLength="575" lengthAdjust="spacingAndGlyphs">California</text>

  <rect class="ribbon-artwork" x="110" y="325" width="164" height="284" rx="18"
        fill="url(#ribbon-tones)" role="img"
        aria-label="Awareness ribbon artwork in green and sunset tones"/>

  <text class="plate-number" x="315" y="598" textLength="752" lengthAdjust="spacingAndGlyphs">NEWPL8</text>

  <text class="plate-slogan" x="312" y="662" textLength="566" lengthAdjust="spacingAndGlyphs">MENTAL HEALTH AWARENESS</text>
</svg>
</body>
</html>
```